Small Business Consulting Firm Needs Business Card Design

Need a sleek modern business card with 2 sides matching the colors of our logo. We will be placing these with a mailer we are sending out. These business cards will only ever be given to business owners. We operate helping businesses who are struggling with cash flow or finances. If the green and blue design needs to be moved to the right of "Brightpath Ledger Consulting" for aesthetic purposes that is ok. We will need an editable file if possible. We would like to include the reps name, email, website, and phone number. For now just use Owen Parrish, oparrish@brightpathledger.com, www.brightpathledger.com, and 855-219-7038.

```html
<!DOCTYPE html>
<html lang="en">
<head>
<meta charset="UTF-8">
<title>Brightpath Ledger Consulting – Business Card</title>
<link href="https://fonts.googleapis.com/css2?family=Open+Sans:wght@400;600&display=swap" rel="stylesheet">
<style>
  :root {
    --blue: #0a7ac9;
    --blue-deep: #0666ad;
    --green: #5faa2c;
    --green-dark: #4a9022;
    --ink: #4a4a4a;
    --paper: #ffffff;
    --backdrop: #e6e8eb;
  }
  * { box-sizing: border-box; margin: 0; padding: 0; }
  html, body { width: 1200px; height: 900px; overflow: hidden; }
  body {
    background: var(--backdrop);
    font-family: "Open Sans", Arial, sans-serif;
    display: flex;
    flex-direction: column;
    align-items: center;
    justify-content: center;
    gap: 56px;
  }
  .card {
    width: 588px;
    height: 336px;
    border-radius: 16px;
    position: relative;
    overflow: hidden;
    box-shadow: 0 6px 18px rgba(0,0,0,0.18);
  }
  /* Front */
  .card-front {
    background: linear-gradient(135deg, #1488d6 0%, var(--blue) 55%, var(--blue-deep) 100%);
    display: flex;
    align-items: center;
    justify-content: center;
  }
  .brand {
    display: flex;
    flex-direction: column;
    align-items: center;
    gap: 14px;
  }
  .brand-mark {
    width: 40px; height: 40px;
    background: currentColor;
  }
  .brand-name {
    font-weight: 400;
    font-size: 24px;
    letter-spacing: 1.5px;
    text-transform: uppercase;
    text-align: center;
    line-height: 1.3;
  }
  .card-front .brand { color: var(--paper); }
  /* Back */
  .card-back { background: var(--paper); }
  .card-back .brand {
    position: absolute;
    left: 40px; top: 100px;
    width: 230px;
    color: var(--ink);
    gap: 12px;
  }
  .card-back .brand-name { font-size: 17px; letter-spacing: 1.2px; }
  .card-back .brand-mark { width: 32px; height: 32px; background: var(--green); }
  .divider {
    position: absolute;
    left: 292px; top: 56px;
    width: 1px; height: 140px;
    background: var(--green);
  }
  .rep {
    position: absolute;
    left: 316px; top: 44px;
    color: var(--ink);
    z-index: 1;
  }
  .rep-name { font-size: 25px; font-weight: 600; line-height: 1.1; }
  .rep-name .first { color: var(--green); }
  .rep-name .last { color: var(--blue); font-weight: 400; }
  .rep-title { font-size: 13px; font-weight: 600; margin-top: 2px; }
  .contacts { list-style: none; margin-top: 12px; font-size: 12.5px; line-height: 1.6; }
  .contacts li { display: flex; align-items: center; gap: 9px; }
  .contacts svg { width: 11px; height: 11px; fill: var(--green); flex: none; }
  .swoosh { position: absolute; left: 0; top: 0; width: 588px; height: 336px; }
</style>
</head>
<body>
  <section class="card card-front">
    <div class="brand">
      <span class="brand-mark"></span>
      <span class="brand-name">Brightpath Ledger<br>Consulting</span>
    </div>
  </section>

  <section class="card card-back">
    <svg class="swoosh" viewBox="0 0 588 336" aria-hidden="true">
      <path d="M0 312 C220 290 430 258 588 226 L588 336 L0 336 Z" fill="var(--blue)"/>
      <path d="M257 281 C380 255 500 225 588 204 L588 196 C500 218 380 250 257 281 Z" fill="var(--green)"/>
      <path d="M300 272 C410 248 510 222 588 212 L588 209 C510 218 410 244 300 272 Z" fill="var(--green-dark)"/>
    </svg>
    <div class="brand">
      <span class="brand-mark"></span>
      <span class="brand-name">Brightpath Ledger<br>Consulting</span>
    </div>
    <div class="divider"></div>
    <div class="rep">
      <p class="rep-name"><span class="first">Owen</span> <span class="last">Parrish</span></p>
      <p class="rep-title">Project Manager</p>
      <ul class="contacts">
        <li><svg viewBox="0 0 12 12"><path d="M2.5 1l2 2-1 1.5c.8 1.5 2 2.7 3.5 3.5L8.5 7l2 2-1.5 2C5 10.5 1.5 7 1 3z"/></svg>855-219-7038</li>
        <li><svg viewBox="0 0 12 12"><path d="M3 0h6v12H3zM4 1.5v8h4v-8z"/></svg>678-402-5516(office)</li>
        <li><svg viewBox="0 0 12 12"><path d="M0 2h12v8H0zM1 3l5 3.5L11 3z"/></svg>oparrish@brightpathledger.com</li>
        <li><svg viewBox="0 0 12 12"><circle cx="6" cy="6" r="5.5"/></svg>www.brightpathledger.com</li>
      </ul>
    </div>
  </section>
</body>
</html>
```